A5 brochure for a double glazed window company - design only

We have an a4 brochure currently and would like to go to an A5 and revamp it. We are a business in Canberra, Australia and it is handed out to the public. It will be 3 A5 sheets back to back to make a 6 page booklet with front and back covers. There will be photos and graphics.

We love our current brochure and can provide it for inspiration - we always get great feedback on the brochure. Happy to have some improvements to take it to the next level.

Documents will be provided once successful with the tender.

Our website is www.brindlepane.com.au
facebook www.facebook.com/brindlepane

Target Market(s)

People wanting to have a more energy efficient home through double glazing

Industry/Entity Type

Construction

Font styles to use
Sans Serif

Colors
33a6d7
3377b5
0355a3
85cae6
cee9f5
cedeed
eaf1f7
0292cd

Requirements
Must have
• A perception of confidence and pull the reader to book an appointment with us. Authorities on double glazing
Nice to have
• lots of soothing blues
Should not have
• tones outside of blues, greys, black
• The brochure I have attached is merely for looks and the front and back pages - content is changing.

```html
<!DOCTYPE html>
<html lang="en">
<head>
<meta charset="utf-8">
<title>Message from the CEO</title>
<link href="https://fonts.googleapis.com/css2?family=Open+Sans:ital,wght@0,400;0,600;1,400;1,600;1,700&display=swap" rel="stylesheet">
<style>
  :root {
    --sky: #33a6d7;
    --mid-blue: #3377b5;
    --deep-blue: #0355a3;
    --light-blue: #85cae6;
    --pale-blue: #cee9f5;
    --mist: #cedeed;
    --ice: #eaf1f7;
    --bright-blue: #0292cd;
    --ink: #2f3a4a;
    --white: #ffffff;
  }
  * { margin: 0; padding: 0; box-sizing: border-box; }
  html, body { width: 847px; height: 1200px; overflow: hidden; background: var(--white); }
  body { font-family: "Open Sans", Arial, sans-serif; color: var(--ink); position: relative; }

  .section-band {
    position: absolute; left: 0; width: 847px; height: 36px;
    background: linear-gradient(90deg, var(--mist) 0%, var(--ice) 55%, var(--white) 100%);
    border-top: 1px solid var(--light-blue);
  }
  .section-band h2 {
    font-style: italic; font-weight: 700; font-size: 19px; color: var(--deep-blue);
    line-height: 36px; padding-left: 44px;
  }
  .ceo-band { top: 40px; }
  .testimonial-band { top: 988px; }

  .ceo-quote {
    position: absolute; left: 44px; top: 92px; width: 505px;
    font-style: italic; font-size: 15.5px; line-height: 21px; color: var(--ink);
  }
  .ceo-quote .open-mark { font-weight: 700; font-size: 26px; color: var(--deep-blue); line-height: 0; vertical-align: -6px; }

  .ceo-portrait {
    position: absolute; left: 580px; top: 90px; width: 236px; height: 262px;
    background: linear-gradient(160deg, var(--mist) 0%, var(--light-blue) 55%, var(--mid-blue) 100%);
    border: 3px solid var(--white); box-shadow: 0 0 0 1px var(--mist);
  }
  .ceo-caption {
    position: absolute; left: 580px; top: 358px; width: 236px; text-align: center;
    font-style: italic; font-size: 13px; color: var(--ink);
  }

  .benefits-band {
    position: absolute; left: 0; top: 392px; width: 847px; height: 140px;
    background: linear-gradient(180deg, var(--mid-blue) 0%, var(--bright-blue) 55%, var(--sky) 100%);
    color: var(--white); font-style: italic;
  }
  .benefits-band .lead { position: absolute; left: 44px; top: 14px; font-size: 15px; }
  .benefits-list { position: absolute; left: 120px; top: 46px; list-style: none; font-size: 15px; line-height: 27px; }
  .benefits-list li span { display: inline-block; width: 36px; }

  .body-columns {
    position: absolute; left: 44px; top: 556px; width: 760px;
    column-count: 2; column-gap: 34px;
    font-style: italic; font-size: 14.3px; line-height: 20px; text-align: justify;
  }
  .body-columns p { margin-bottom: 12px; }
  .signature {
    position: absolute; right: 44px; top: 912px;
    font-style: italic; font-size: 14.5px;
  }
</style>
</head>
<body>
  <header class="section-band ceo-band"><h2>Message from the CEO</h2></header>

  <p class="ceo-quote"><span class="open-mark">“</span>My vision is for every home in Canberra to be double glazed. I have been harping on about this since 2006 and it still amazes me how many new homes have single glazed aluminium installed because they are the cheapest window and door that you can buy. Well, my question is, why aren't you leaving the insulation out of your walls and ceiling? The window and door openings are a missed opportunity to have a fully insulated home.</p>

  <div class="ceo-portrait" role="img" aria-label="Portrait photo of the CEO, Maren Doyle"></div>
  <p class="ceo-caption">Maren Doyle, CEO</p>

  <section class="benefits-band">
    <p class="lead">The benefits from insulating your home properly are that you will:</p>
    <ol class="benefits-list">
      <li><span>1.</span>Have a more temperate home which gives you immense comfort</li>
      <li><span>2.</span>Your heating and cooling bills will be reduced</li>
      <li><span>3.</span>Your home will be quiet and serene</li>
    </ol>
  </section>

  <div class="body-columns">
    <p>We have been pulling windows out of existing homes since 2005 and we have so many happy home owners. They regret not doing it early. They have added value to their home, increased their energy star rating and have noticed a drop in their bill by a significant amount.</p>
    <p>I operate a unique business in Canberra that gives amazing local service to home owners and future home owners. We are not a supplier, we are a business that works with you on your behalf to find the best match of windows and doors to your home. We take the burden off you and gather quotes, organise your order, delivery, installation and any after sales service calls. All of our products are Australian made.</p>
    <p>Our clients always comment on the individual service that they receive from us and many have become friends of our team.</p>
    <p>Do yourself a favour today, invest in yourself and your home and change your windows and doors to double glazed ones. Our windows and doors will make a difference, we guarantee it. Book in a free consultation with myself and reap the rewards.”</p>
  </div>
  <p class="signature">Maren Doyle</p>

  <header class="section-band testimonial-band"><h2>Testimonial from client</h2></header>
</body>
</html>
```